Brixtondel - eCommerce Design and Shopify Theme customisation

eCommerce Website Design - firstly with mockups then once we have chosen the design the successful designer will need to choose, purchase and customise a Shopify theme to match the design. We have a logo already designed and now want to create our web presence based on carrying up to 50 products on our website.
Target Market(s)
UK Pet Owners
Industry/Entity Type
Pet Shop
Requirements
Must have
- Design must be achievable using a customised Shopify theme - the successful designer will be responsible for the delivery of a working theme on our shopify website.
Should not have
- should not look cheap or have designs that aren't compatible or achievable with Shopify

```html
<!DOCTYPE html>
<html lang="en">
<head>
<meta charset="utf-8">
<title>Brixtondel – Pet Shop</title>
<link href="https://fonts.googleapis.com/css2?family=Questrial&family=Poppins:wght@400;500;600&display=swap" rel="stylesheet">
<style>
:root{
  --black:#141414;
  --yellow:#f9c20c;
  --sky:#3ba6de;
  --purple:#8d5fb3;
  --teal:#2db6a0;
  --pink:#e2479b;
  --grey-bg:#f4f4f4;
  --text:#222;
  --muted:#777;
  --white:#fff;
  --price:#9a9a9a;
}
*{margin:0;padding:0;box-sizing:border-box}
html,body{width:1200px;height:4255px;overflow:hidden}
body{position:relative;background:var(--white);font-family:"Poppins",sans-serif;color:var(--text);font-size:13px}
.abs{position:absolute}
.heading{font-family:"Questrial",sans-serif}
.btn{position:absolute;background:var(--yellow);color:var(--black);font:500 14px "Poppins",sans-serif;display:flex;align-items:center;justify-content:center;text-transform:uppercase;letter-spacing:.3px}

/* Header */
.site-header{left:0;top:0;width:1200px;height:72px;background:var(--black)}
.brand{left:80px;top:10px;display:flex;align-items:center;gap:8px;color:var(--yellow);font:600 17px "Poppins",sans-serif}
.brand-dot{width:22px;height:22px;border-radius:50%;background:var(--yellow)}
.main-nav{left:232px;top:0;height:72px;display:flex;gap:38px;align-items:center;color:var(--white);font-size:15px}
.main-nav .active{color:var(--yellow);border-bottom:2px solid var(--yellow);padding:22px 6px}
.search{left:845px;top:22px;width:185px;height:26px;border:1px solid #bbb;border-radius:14px;color:#ddd;font-size:12px;padding:4px 0 0 28px}
.search svg{position:absolute;left:10px;top:6px}
.header-icon{top:23px}

/* Hero */
.hero{left:0;top:72px;width:1200px;height:685px;background:var(--sky);overflow:hidden}
.hero-circle{left:553px;top:55px;width:540px;height:540px;border-radius:50%;background:var(--yellow)}
.hero-photo{left:580px;top:0;width:480px;height:685px;background:radial-gradient(ellipse at 50% 45%,#e8b877 0%,#d49a55 45%,rgba(212,154,85,0) 72%)}
.hero-kicker{left:80px;top:262px;font-size:40px;color:var(--black)}
.hero-title{left:80px;top:300px;font-size:60px;color:var(--black)}
.hero-text{left:80px;top:375px;font-size:12px;color:#1b3f58}
.hero-dots{left:583px;top:656px;display:flex;gap:10px}
.hero-dots span{width:10px;height:10px;border-radius:50%;background:var(--black)}
.hero-dots span+span{background:var(--yellow)}

/* Service strip */
.service{top:786px;width:338px;height:99px;display:flex;align-items:center;justify-content:center;gap:16px;color:var(--white);font-size:18px}

/* Section titles */
.section-title{left:0;width:1200px;text-align:center;font-size:30px;color:var(--black)}
.section-sub{left:0;width:1200px;text-align:center;font-size:12px;color:#444}

/* Promo */
.promo{top:1013px;width:517px;height:264px;overflow:hidden}
.promo-title{font-size:28px;color:var(--white);text-transform:uppercase}
.promo-text{font-size:12px;color:var(--white);width:210px;line-height:1.4}

/* Products */
.filters{left:0;width:1200px;top:1364px;display:flex;justify-content:center;gap:22px;font-size:12px;color:#333}
.product-img{top:1418px;width:250px;height:324px;background:#f3f3f3}
.product-shape{position:absolute;left:40px;top:80px;width:170px;height:160px;border-radius:20px}
.product-name{top:1758px;font-size:13px;color:var(--black);text-transform:uppercase}
.stars{color:var(--yellow);font-size:13px;letter-spacing:1px}
.price{top:1803px;font-size:22px;color:var(--price);text-decoration:line-through}
.slider-arrow{top:1558px;width:50px;height:50px;border-radius:50%;display:flex;align-items:center;justify-content:center}

/* Categories */
.categories{left:0;top:1977px;width:1200px;height:491px;background:var(--grey-bg);overflow:hidden}
.cat-heading{top:2093px;font-size:28px;color:var(--black)}
.cat-list{list-style:none;font-size:13px;color:#333}
.cat-list li{height:38.6px;display:flex;align-items:center;gap:14px}
.cat-list li::before{content:"";width:8px;height:8px;border-radius:50%;background:var(--teal)}
.cat-list.right{text-align:right}
.cat-list.right li{justify-content:flex-end}
.cat-list.right li::before{order:2}
.pets-circle{left:415px;width:370px;height:370px;border-radius:50%;background:var(--yellow)}
.pets-photo{left:445px;width:320px;height:348px;background:radial-gradient(ellipse at 50% 50%,#e6c8a1 0%,#b7aaa0 50%,rgba(183,170,160,0) 75%)}

/* Blog */
.blog-card{top:2576px;width:332px;height:460px;background:#f5f5f5}
.blog-img{position:absolute;left:0;top:0;width:332px;height:227px}
.date-badge{position:absolute;left:128px;top:185px;width:68px;height:68px;border-radius:50%;background:var(--pink);border:4px solid var(--white);color:var(--white);display:flex;flex-direction:column;align-items:center;justify-content:center;font-size:15px;line-height:1.1}
.date-badge small{font-size:9px}
.blog-title{position:absolute;left:20px;top:272px;font-size:20px;color:var(--black)}
.blog-text{position:absolute;left:20px;top:308px;width:290px;font-size:12px;line-height:1.4;color:#444}
.read-more{position:absolute;left:20px;top:412px;font-size:12px;color:var(--yellow);text-transform:uppercase}

/* Testimonials */
.testimonials{left:0;top:3183px;width:1200px;height:386px;background:var(--grey-bg)}

/* Newsletter */
.news-input{left:318px;top:3711px;width:382px;height:50px;background:#f0f0f0;color:#999;font-size:12px;font-style:italic;padding:17px 0 0 24px}
.footer-brand{left:0;width:1200px;top:3835px;text-align:center;font:600 26px "Poppins",sans-serif;color:var(--black)}

/* Footer */
.site-footer{left:0;top:3893px;width:1200px;height:362px;background:var(--black);color:var(--white)}
.foot-heading{top:73px;font-size:19px}
.foot-list{list-style:none;font-size:13px;line-height:1.35}
.foot-list li::before{content:"•";color:var(--yellow);margin-right:10px}
.contact-row{display:flex;gap:12px;align-items:flex-start;font-size:13px;line-height:1.3;margin-bottom:3px}
.social{width:26px;height:26px;border-radius:50%;background:var(--yellow)}
.foot-rule{left:80px;top:277px;width:1041px;height:1px;background:#333}
.pay-card{top:300px;width:42px;height:27px;border-radius:3px;background:#e8e8e8}
</style>
</head>
<body>

<!-- Header -->
<header class="abs site-header">
  <div class="abs brand"><span class="brand-dot"></span>Brixtondel</div>
  <nav class="abs main-nav">
    <span class="active">Home</span><span>Dog</span><span>Cat</span><span>Shop</span><span>Blog</span><span>Contact</span><span>Offers</span>
  </nav>
  <div class="abs search">
    <svg width="12" height="12" viewBox="0 0 12 12"><circle cx="5" cy="5" r="4" fill="none" stroke="#ddd" stroke-width="1.5"/><line x1="8" y1="8" x2="11" y2="11" stroke="#ddd" stroke-width="1.5"/></svg>Search
  </div>
  <svg class="abs header-icon" style="left:1057px" width="22" height="24" viewBox="0 0 22 24"><circle cx="11" cy="7" r="5" fill="none" stroke="#fff" stroke-width="1.8"/><path d="M2 22c1-6 17-6 18 0" fill="none" stroke="#fff" stroke-width="1.8"/></svg>
  <svg class="abs header-icon" style="left:1110px" width="24" height="24" viewBox="0 0 24 24"><path d="M5 8h14l-1 14H6z" fill="none" stroke="#fff" stroke-width="1.8"/><path d="M8 8a4 4 0 0 1 8 0" fill="none" stroke="#fff" stroke-width="1.8"/></svg>
</header>

<!-- Hero -->
<section class="abs hero">
  <div class="abs hero-circle"></div>
  <div class="abs hero-photo" role="img" aria-label="Photo of a golden retriever puppy sitting with its tongue out"></div>
  <div class="abs heading hero-kicker">Best Selling</div>
  <h1 class="abs heading hero-title" style="font-weight:400">Dog Products</h1>
  <p class="abs hero-text">Lorem Ipsum is simply dummy text of the printing and typesetting industry.</p>
  <div class="btn" style="left:80px;top:430px;width:178px;height:51px">Shop Now</div>
  <div class="abs hero-dots"><span></span><span></span></div>
</section>

<!-- Services -->
<div class="abs service" style="left:80px;background:var(--purple)">
  <svg width="44" height="30" viewBox="0 0 44 30"><rect x="2" y="4" width="24" height="18" fill="none" stroke="#fff" stroke-width="2"/><path d="M26 10h9l6 7v5H26" fill="none" stroke="#fff" stroke-width="2"/><circle cx="10" cy="25" r="3" fill="var(--purple)" stroke="#fff" stroke-width="2"/><circle cx="34" cy="25" r="3" fill="var(--purple)" stroke="#fff" stroke-width="2"/></svg>Free Delivery
</div>
<div class="abs service" style="left:431px;background:var(--teal)">
  <svg width="34" height="34" viewBox="0 0 34 34"><path d="M6 20v-4a11 11 0 0 1 22 0v4" fill="none" stroke="#fff" stroke-width="2"/><rect x="4" y="18" width="6" height="9" rx="2" fill="none" stroke="#fff" stroke-width="2"/><rect x="24" y="18" width="6" height="9" rx="2" fill="none" stroke="#fff" stroke-width="2"/></svg>Premim Support
</div>
<div class="abs service" style="left:783px;background:var(--pink)">
  <svg width="32" height="34" viewBox="0 0 32 34"><rect x="4" y="3" width="24" height="28" rx="2" fill="none" stroke="#fff" stroke-width="2"/><path d="M10 17a6 6 0 1 0 6-6h-3l2-2" fill="none" stroke="#fff" stroke-width="2"/></svg>Return Policy
</div>

<!-- Summer fun promos -->
<h2 class="abs heading section-title" style="top:918px;font-weight:400">Summer Fun for your Pets</h2>
<p class="abs section-sub" style="top:965px">this will be altered to Winter fun for your pets in October</p>

<div class="abs promo" style="left:80px;background:linear-gradient(90deg,#b8752c 0%,#d8a055 60%,#c78a45 100%)" role="img" aria-label="Photo of a happy terrier puppy on a warm background">
  <div class="abs heading promo-title" style="left:35px;top:25px">New Arrival</div>
  <p class="abs promo-text" style="left:35px;top:65px">Lorem Ipsum is simply dummy text of the printing and typesetting industry.</p>
  <div class="btn" style="left:35px;top:118px;width:178px;height:51px">Shop Now</div>
</div>
<div class="abs promo" style="left:604px;background:linear-gradient(90deg,#7b6a58 0%,#a9957f 55%,#c9b298 100%)" role="img" aria-label="Photo of a tabby cat looking at the camera">
  <div class="abs heading" style="left:290px;top:30px;font-size:18px;color:#fff">Discount Voucher</div>
  <p class="abs promo-text" style="left:290px;top:56px;width:190px">Lorem Ipsum is simply dummy text of the printing and typesetting.</p>
  <div class="btn" style="left:295px;top:113px;width:178px;height:51px">Shop Now</div>
</div>

<!-- Feature products -->
<h2 class="abs heading section-title" style="top:1305px;font-weight:400">Feature Products</h2>
<div class="abs filters"><span>ALL</span><span>New Arrival</span><span>Best Seller</span><span>Discounted</span></div>

<div class="abs product-img" style="left:80px" role="img" aria-label="Product photo of a brown dog bed with bumpers"><div class="product-shape" style="background:#c9b08f;top:110px;height:110px"></div></div>
<div class="abs product-img" style="left:343px" role="img" aria-label="Product photo of an automatic cat feeder"><div class="product-shape" style="background:#b8b8b8;left:65px;width:120px"></div></div>
<div class="abs product-img" style="left:604px" role="img" aria-label="Product photo of a stainless steel dog bowl"><div class="product-shape" style="background:#5fb3d8;top:120px;height:90px;border-radius:50%"></div></div>
<div class="abs product-img" style="left:868px" role="img" aria-label="Product photo of a white robotic mouse cat toy"><div class="product-shape" style="background:#e2e2e2;top:120px;height:90px;border-radius:50%"></div></div>

<div class="abs slider-arrow" style="left:55px;background:#555">
  <svg width="14" height="14" viewBox="0 0 14 14"><path d="M9 2L4 7l5 5" fill="none" stroke="#fff" stroke-width="2"/></svg>
</div>
<div class="abs slider-arrow" style="left:1096px;background:var(--yellow)">
  <svg width="14" height="14" viewBox="0 0 14 14"><path d="M5 2l5 5-5 5" fill="none" stroke="#000" stroke-width="2"/></svg>
</div>

<div class="abs product-name" style="left:80px">Dog Bed W Bumpers</div>
<div class="abs product-name" style="left:343px">Automatic Cat Feeder</div>
<div class="abs product-name" style="left:604px">Stainless Steel Dog Bowl</div>
<div class="abs product-name" style="left:868px">Mouse Robotic Cat Toy (White)</div>
<div class="abs stars" style="left:80px;top:1779px">★★★★<span style="color:#ccc">★</span></div>
<div class="abs stars" style="left:343px;top:1779px">★★★★<span style="color:#ccc">★</span></div>
<div class="abs stars" style="left:604px;top:1779px">★★★★★</div>
<div class="abs stars" style="left:868px;top:1779px">★★★★★</div>
<div class="abs price" style="left:80px">$39.90</div>
<div class="abs price" style="left:343px">$70.99</div>
<div class="abs price" style="left:604px">$14.99</div>
<div class="abs price" style="left:868px">$9.99</div>

<div class="btn" style="left:511px;top:1881px;width:178px;height:51px">Browse More</div>

<!-- Categories -->
<section class="abs categories">
  <div class="abs pets-circle" style="top:93px"></div>
  <div class="abs pets-photo" style="top:143px" role="img" aria-label="Photo of a spaniel puppy and a grey cat side by side"></div>
</section>
<h2 class="abs heading section-title" style="top:2006px;font-weight:400">Summer Fun for your Pets</h2>
<p class="abs section-sub" style="top:2053px">this will be altered to Winter fun for your pets in October</p>
<div class="abs heading cat-heading" style="left:80px">For your Dogs</div>
<div class="abs heading cat-heading" style="right:80px">For your Cats</div>
<ul class="abs cat-list" style="left:80px;top:2154px">
  <li>Orthopedic Dog Beds</li><li>Vet Bed</li><li>Cool Coats</li><li>Slow Feed Dog Bowls</li><li>Automatic Dog Feeder</li><li>Drinking Fountain</li><li>Collapsible Drinking Bowls</li>
</ul>
<ul class="abs cat-list right" style="right:80px;top:2154px">
  <li>Beautiful Cat Beds</li><li>Vet Bed</li><li>Cat Nip Toys</li><li>Scratch Posts</li><li>Automatic Cat Feeder</li><li>Drinking Fountain</li>
</ul>

<!-- Blog -->
<h2 class="abs heading section-title" style="top:2505px;font-weight:400">Blog Posts</h2>

<article class="abs blog-card" style="left:80px">
  <div class="blog-img" style="background:linear-gradient(135deg,#d9cfc2,#b9a894)" role="img" aria-label="Photo of a small dog resting in a grey pet bed"></div>
  <div class="date-badge">MAY<small>05.2019</small></div>
  <h3 class="blog-title heading" style="font-weight:400">Blog Posts• 01</h3>
  <p class="blog-text">Lorem Ipsum is simply dummy text of the printing and typesetting industry. Lorem Ipsum has been the industry's standard dummy text ever since the 1500s.</p>
  <span class="read-more">Read More</span>
</article>
<article class="abs blog-card" style="left:434px">
  <div class="blog-img" style="background:linear-gradient(135deg,#c9c4c0,#e6c3c8)" role="img" aria-label="Photo of a grey kitten playing with a pink toy"></div>
  <div class="date-badge">MAY<small>05.2019</small></div>
  <h3 class="blog-title heading" style="font-weight:400">Blog Posts• 02</h3>
  <p class="blog-text">Lorem Ipsum is simply dummy text of the printing and typesetting industry. Lorem Ipsum has been the industry's standard dummy text ever since the 1500s.</p>
  <span class="read-more">Read More</span>
</article>
<article class="abs blog-card" style="left:789px">
  <div class="blog-img" style="background:linear-gradient(135deg,#d8c3a0,#a88c62)" role="img" aria-label="Photo of a dog eating from a metal bowl"></div>
  <div class="date-badge">MAY<small>05.2019</small></div>
  <h3 class="blog-title heading" style="font-weight:400">Blog Posts• 03</h3>
  <p class="blog-text">Lorem Ipsum is simply dummy text of the printing and typesetting industry. Lorem Ipsum has been the industry's standard dummy text ever since the 1500s.</p>
  <span class="read-more">Read More</span>
</article>

<div class="btn" style="left:511px;top:3081px;width:178px;height:51px">Browse More</div>

<!-- Testimonials -->
<section class="abs testimonials"></section>
<h2 class="abs heading section-title" style="top:3234px;font-weight:400">Our Clients Say's</h2>
<p class="abs section-sub" style="top:3300px;left:285px;width:630px;line-height:1.45">Lorem Ipsum is simply dummy text of the printing and typesetting industry. Lorem Ipsum has been the industry's standard dummy text ever since the 1500s.</p>
<div class="abs stars" style="left:0;width:1200px;top:3346px;text-align:center">★★★★★</div>
<div class="abs heading" style="left:0;width:1200px;top:3380px;text-align:center;font-size:20px">Mara Lind</div>
<div class="abs" style="left:578px;top:3430px;display:flex;gap:10px">
  <span style="width:6px;height:6px;border-radius:50%;background:var(--yellow)"></span>
  <span style="width:6px;height:6px;border-radius:50%;background:#000"></span>
  <span style="width:6px;height:6px;border-radius:50%;background:#000"></span>
</div>
<div class="btn" style="left:511px;top:3470px;width:178px;height:51px">Browse More</div>

<!-- Newsletter -->
<h2 class="abs heading section-title" style="top:3640px;font-weight:400">Subscribe &nbsp;Our Newsletter</h2>
<div class="abs news-input">Email Address</div>
<div class="btn" style="left:700px;top:3711px;width:180px;height:50px">Subscribe</div>
<div class="abs footer-brand">Brixtondel</div>

<!-- Footer -->
<footer class="abs site-footer">
  <div class="abs heading foot-heading" style="left:80px">About us</div>
  <div class="abs heading foot-heading" style="left:468px">Quick Links</div>
  <div class="abs heading foot-heading" style="left:735px">Accounts</div>
  <div class="abs heading foot-heading" style="left:950px">Contact Detail</div>

  <p class="abs" style="left:80px;top:126px;width:300px;font-size:13px;line-height:1.4">Lorem Ipsum is simply dummy text of the printing and typesetting industry.</p>
  <span class="abs" style="left:80px;top:172px;font-size:13px;color:var(--yellow);text-decoration:underline">READ MORE</span>
  <div class="abs" style="left:80px;top:205px;display:flex;gap:10px">
    <span class="social"></span><span class="social"></span><span class="social"></span><span class="social"></span><span class="social"></span>
  </div>

  <ul class="abs foot-list" style="left:468px;top:126px"><li>Home</li><li>Dog</li><li>Cat</li><li>Shop</li><li>Blog</li><li>Contact</li><li>Offers</li></ul>
  <ul class="abs foot-list" style="left:735px;top:126px"><li>Login</li><li>Register</li><li>My Profile</li><li>My Cart</li><li>Checkout</li></ul>

  <div class="abs" style="left:950px;top:126px">
    <div class="contact-row"><svg width="12" height="14" viewBox="0 0 12 14"><path d="M2 1h3l1 3-2 1a7 7 0 0 0 4 4l1-2 3 1v3a1 1 0 0 1-1 1A11 11 0 0 1 1 2a1 1 0 0 1 1-1z" fill="var(--yellow)"/></svg>(+012) 555 010 2</div>
    <div class="contact-row"><svg width="12" height="14" viewBox="0 0 12 14"><path d="M2 1h3l1 3-2 1a7 7 0 0 0 4 4l1-2 3 1v3a1 1 0 0 1-1 1A11 11 0 0 1 1 2a1 1 0 0 1 1-1z" fill="var(--yellow)"/></svg>(+012) 555 010 3</div>
    <div class="contact-row"><svg width="12" height="14" viewBox="0 0 12 14"><rect x="0" y="3" width="12" height="9" fill="none" stroke="var(--yellow)" stroke-width="1.5"/><path d="M0 3l6 5 6-5" fill="none" stroke="var(--yellow)" stroke-width="1.5"/></svg>hello@brixtondel.com</div>
    <div class="contact-row"><svg width="12" height="14" viewBox="0 0 12 14"><path d="M6 13S1 8 1 5a5 5 0 0 1 10 0c0 3-5 8-5 8z" fill="var(--yellow)"/><circle cx="6" cy="5" r="2" fill="#141414"/></svg><span>48 Harbour Lane,<br>Elmsford</span></div>
  </div>

  <div class="abs foot-rule"></div>
  <p class="abs" style="left:80px;top:306px;font-size:13px">Copyright © 2019 Brixtondel. All rights reserved.</p>
  <div class="abs pay-card" style="left:935px"></div>
  <div class="abs pay-card" style="left:983px"></div>
  <div class="abs pay-card" style="left:1031px"></div>
  <div class="abs pay-card" style="left:1079px"></div>
</footer>

</body>
</html>
```